New Business Card Design Project

We want a modern business card that catches the attention of other remodeling companies as well as homeowners. We would like it to be informative but still simple.

Target Market(s)

Residential and other Business's

Contact Information for Business Card

TrellBrix
Phone number is 5153927048
Address is
4817 SW 3rd Lane
Ankeny, Iowa 50023
email is trellbrixco@quamlet.com

Requirements
Must have
• Our tagline
• Honest | Professional | Affordable

```html
<!DOCTYPE html>
<html lang="en">
<head>
<meta charset="utf-8">
<title>TrellBrix Business Card</title>
<link rel="stylesheet" href="https://fonts.googleapis.com/css2?family=Open+Sans:wght@400;600;800&family=Oswald:wght@600&display=swap">
<style>
  :root {
    --brand-blue: #2660a8;
    --brand-orange: #d4501f;
    --paper: #f5f5f5;
    --ink: #1f1f1f;
    --stage: #e4e6e9;
  }
  * { box-sizing: border-box; margin: 0; padding: 0; }
  html, body { width: 1200px; height: 1021px; overflow: hidden; }
  body {
    background: var(--stage);
    font-family: "Open Sans", sans-serif;
    position: relative;
  }
  .card {
    position: absolute;
    left: 220px;
    width: 760px;
    height: 434px;
    box-shadow: 0 6px 18px rgba(0,0,0,.18);
    overflow: hidden;
  }
  .card-back { top: 46px; background: var(--brand-blue); }
  .card-front { top: 540px; background: var(--paper); }

  .brand {
    position: absolute;
    left: 0; right: 0;
    display: flex;
    flex-direction: column;
    align-items: center;
  }
  .card-back .brand { top: 135px; }
  .card-front .brand { top: 62px; }

  .brand-name {
    display: flex;
    align-items: center;
    gap: 14px;
    font-family: "Open Sans", sans-serif;
    font-weight: 800;
    font-size: 76px;
    line-height: 1;
    letter-spacing: 1px;
  }
  .brand-dot {
    width: 26px; height: 26px;
    border-radius: 50%;
    background: var(--brand-orange);
  }
  .card-back .brand-name { color: #ffffff; }
  .card-front .brand-name { color: var(--brand-blue); }

  .tagline {
    margin-top: 14px;
    font-family: "Oswald", sans-serif;
    font-weight: 600;
    font-size: 24px;
    letter-spacing: 1.5px;
    text-transform: uppercase;
  }
  .card-back .tagline { color: #ffffff; }
  .card-front .tagline { color: var(--brand-blue); }
  .tagline .sep { color: var(--brand-orange); margin: 0 8px; }

  .person {
    position: absolute;
    left: 40px;
    top: 260px;
    width: 270px;
    text-align: right;
  }
  .person-name {
    color: var(--brand-blue);
    font-weight: 600;
    font-size: 27px;
    line-height: 1.2;
  }
  .person-role {
    color: var(--ink);
    font-size: 20px;
    margin-top: 2px;
  }
  .divider {
    position: absolute;
    left: 335px;
    top: 262px;
    width: 2px;
    height: 110px;
    background: var(--brand-orange);
  }
  .contact {
    position: absolute;
    left: 362px;
    top: 258px;
    color: var(--ink);
    font-size: 21px;
    line-height: 1.4;
  }
  .contact-line { display: flex; align-items: center; gap: 10px; }
  .contact-line svg { width: 18px; height: 18px; flex: none; }

  .stripe {
    position: absolute;
    bottom: 0;
    height: 16px;
  }
  .stripe-blue { left: 0; width: 432px; background: var(--brand-blue); }
  .stripe-orange { left: 438px; right: 0; background: var(--brand-orange); }
</style>
</head>
<body>

<section class="card card-back">
  <div class="brand">
    <div class="brand-name"><span>TrellBrix</span><span class="brand-dot"></span></div>
    <div class="tagline">Honest<span class="sep">/</span>Professional<span class="sep">/</span>Affordable</div>
  </div>
</section>

<section class="card card-front">
  <div class="brand">
    <div class="brand-name"><span>TrellBrix</span><span class="brand-dot"></span></div>
    <div class="tagline">Honest<span class="sep">/</span>Professional<span class="sep">/</span>Affordable</div>
  </div>

  <div class="person">
    <div class="person-name">Daniel Whitmore</div>
    <div class="person-role">Owner</div>
  </div>

  <div class="divider"></div>

  <div class="contact">
    <div class="contact-line">4817 SW 3rd Lane</div>
    <div class="contact-line">Ankeny, Iowa 50023</div>
    <div class="contact-line">
      <svg viewBox="0 0 24 24" aria-hidden="true"><path fill="#d4501f" d="M6.6 10.8a15.1 15.1 0 0 0 6.6 6.6l2.2-2.2a1 1 0 0 1 1-.25 11.4 11.4 0 0 0 3.6.6 1 1 0 0 1 1 1V20a1 1 0 0 1-1 1A17 17 0 0 1 3 4a1 1 0 0 1 1-1h3.5a1 1 0 0 1 1 1c0 1.25.2 2.45.6 3.6a1 1 0 0 1-.25 1z"/></svg>
      <span>515-392-7048</span>
    </div>
    <div class="contact-line">
      <svg viewBox="0 0 24 24" aria-hidden="true"><rect x="2.5" y="5" width="19" height="14" fill="none" stroke="#d4501f" stroke-width="2"/><path d="M3 6l9 7 9-7M3 18l7-6M21 18l-7-6" fill="none" stroke="#d4501f" stroke-width="1.6"/></svg>
      <span>trellbrixco@quamlet.com</span>
    </div>
  </div>

  <div class="stripe stripe-blue"></div>
  <div class="stripe stripe-orange"></div>
</section>

</body>
</html>
```